Rudy Fenwick - Free Personalised Health Consultation - "One size does not fit all"

This flyer will be left on tables/seats at speaking events and seminars and used to attain leads.

Top half will have "SMS me for a FREE Personalised Health Consultation" and my picture (see www.rudyfenwick.example and pick most engaging photo) and underneath my contact details. It must have lines with "Notes:" halfway down so people can take notes at the seminar and lines on the back with my contact details again and "Notes: with lines.

I am having a business card also being designed by Artshelf for same and would like the flyer and business card to carry a similar feel/look for consistency.

Below is the brief for the business card being designed:
Business Card for www.rudyfenwick.example site. It is a trust site and I use it for 1:1 relatable connections. It is the one I use for building intimate 1:1 trust building and Exec Coaching Services and programs for high wealth individuals and corporates. I also have a commercial programmatic site of my personal health products and services and programs for main stream one to many. www.quietbirchliving.example that can also provoke thought for the www.rudyfenwick.example business card. (mind you will get a separate business card for that site, but want to provide context). It has a logo which you may want to draw from in designing the rudyfenwick business card which is personal and is about building my brand. There is also a rudyfenwick personal FB page and rudyfenwick business FB page. I am a Certified Talent Compass 3.1 Coach with Harlow and you can get a corporate brief of me on there to give you more context https://www.harlowtalenthub.example/coach/en-us/directory?search=rudy

Target Market(s)

Exec, IT, Health conscious. Corporates wanting to run Health and Wellness programs. Those wanting to go from good to great. Millennials to Middleaged.

Industry/Entity Type

Health And Wellness

Font styles to use
Sans Serif
Other font styles liked:
• Arial and Calibri ok too

Colors

Designer to choose colors to be used in the design.

Requirements
Must have
• Picture of me - use best from www.rudyfenwick.example or can send one you choose.
• Contact details like my buisness card being designed by you guys in separate project.
• Name: Rudy Fenwick
• email: rudy@rudyfenwick.,example
• Phone: Australia +61 400 000 000 Singapore: +65 9000 0000
Nice to have
• Open to ideas

```html
<!DOCTYPE html>
<html lang="en">
<head>
<meta charset="utf-8">
<title>Rudy Fenwick – Free Personalised Health Consultation Flyer</title>
<link rel="stylesheet" href="https://fonts.googleapis.com/css2?family=Montserrat:wght@300;400;600;800&family=Arimo:wght@400&display=swap">
<style>
  :root {
    --stage: #7a7a7a;
    --ink: #0d0d0d;
    --paper: #ffffff;
    --bar: #2b2b2b;
    --hero-dark: #111111;
    --rule: #b9b9b9;
    --soft-rule: #c9c9c9;
    --text-light: #f2f2f2;
    --text-muted: #d6d6d6;
  }
  * { box-sizing: border-box; margin: 0; padding: 0; }
  html, body { width: 768px; height: 1200px; overflow: hidden; }
  body {
    background: var(--stage);
    font-family: "Arimo", Arial, sans-serif;
    position: relative;
  }
  .flyer {
    position: absolute;
    top: 353px;
    width: 350px;
    height: 494px;
    background: var(--paper);
    overflow: hidden;
    box-shadow: 0 10px 18px rgba(0,0,0,0.28);
  }
  .flyer--front { left: 22px; }
  .flyer--back { left: 396px; }

  /* Front hero */
  .hero {
    position: absolute; left: 0; top: 0; width: 350px; height: 283px;
    background: linear-gradient(100deg, #0a0a0a 0%, #161616 45%, #1e1e1e 100%);
  }
  .hero__portrait {
    position: absolute; right: 0; top: 0; width: 175px; height: 263px;
    background: radial-gradient(ellipse at 55% 40%, #8a8a8a 0%, #4a4a4a 45%, #1c1c1c 80%);
  }
  .brand-name {
    position: absolute;
    font-family: "Arimo", Arial, sans-serif;
    font-size: 10px; letter-spacing: 0.3px;
    color: var(--text-light);
    text-transform: uppercase;
  }
  .brand-name .underlined { border-bottom: 1px solid var(--text-light); padding-bottom: 2px; }
  .hero .brand-name { left: 20px; top: 22px; }
  .headline { position: absolute; left: 18px; top: 82px; color: var(--text-light); font-family: "Montserrat", sans-serif; }
  .headline__sms { display: block; font-weight: 800; font-size: 25px; line-height: 28px; }
  .headline__for { display: block; font-weight: 300; font-size: 21px; line-height: 26px; margin-left: 2px; }
  .headline__free {
    display: block; font-weight: 600; font-size: 47px; line-height: 50px;
    color: var(--hero-dark);
    -webkit-text-stroke: 2.6px var(--text-light);
    paint-order: stroke fill;
    letter-spacing: 2px;
  }
  .headline__offer { display: block; font-weight: 400; font-size: 14.5px; line-height: 18px; margin-left: 2px; }

  .contact-bar {
    position: absolute; left: 0; width: 350px; height: 20px;
    background: var(--bar); color: var(--text-muted);
    font-size: 7px; display: flex; align-items: center; justify-content: space-between;
    padding: 0 20px;
  }
  .contact-bar .sep { border-left: 1px solid var(--text-muted); margin: 0 3px; height: 9px; display: inline-block; vertical-align: middle; }
  .contact-bar__email { display: flex; align-items: center; gap: 5px; }
  .flyer--front .contact-bar { top: 263px; }
  .flyer--back .contact-bar { top: 57px; height: 17px; }

  .note-line { position: absolute; left: 18px; right: 26px; height: 1.5px; background: var(--rule); }
  .flyer--back .note-line { background: var(--soft-rule); height: 1px; }

  .footer-rule { position: absolute; left: 0; top: 473px; width: 350px; height: 2px; background: var(--ink); }
  .web-tab {
    position: absolute; left: 226px; top: 464px; width: 124px; height: 19px;
    background: var(--ink); color: var(--text-light);
    font-size: 7px; display: flex; align-items: center; justify-content: center;
  }

  /* Back */
  .back-header { position: absolute; left: 0; top: 0; width: 350px; height: 57px; background: linear-gradient(100deg, #111 0%, #1d1d1d 100%); }
  .back-header .brand-name { left: 0; right: 0; top: 28px; text-align: center; font-size: 10.5px; }
  .back-scene {
    position: absolute; left: 0; top: 74px; width: 350px; height: 420px;
    background: linear-gradient(90deg, #f3f3f3 0%, #ececec 40%, #e6e6e6 60%, #f2f2f2 100%);
  }
</style>
</head>
<body>

<section class="flyer flyer--front" aria-label="Flyer front">
  <div class="hero">
    <div class="hero__portrait" role="img" aria-label="Black and white portrait of Rudy Fenwick, hand at chin, in a white shirt"></div>
    <div class="brand-name">Rudy <span class="underlined">Fenwick</span></div>
    <h1 class="headline">
      <span class="headline__sms">SMS ME</span>
      <span class="headline__for">FOR A</span>
      <span class="headline__free">FREE</span>
      <span class="headline__offer">PERSONALISED<br>HEALTH CONSULTATION</span>
    </h1>
  </div>
  <div class="contact-bar">
    <span>Australia +61 400 000 000 <span class="sep"></span>Singapore: +65 9000 0000</span>
    <span class="contact-bar__email">
      <svg width="10" height="10" viewBox="0 0 10 10" aria-hidden="true"><circle cx="5" cy="5" r="4.4" fill="none" stroke="#d6d6d6" stroke-width="0.7"/><rect x="2.6" y="3.4" width="4.8" height="3.3" fill="none" stroke="#d6d6d6" stroke-width="0.6"/><path d="M2.6 3.4 L5 5.3 L7.4 3.4" fill="none" stroke="#d6d6d6" stroke-width="0.6"/></svg>
      rudy@rudyfenwick.example
    </span>
  </div>
  <div class="note-line" style="top:318px"></div>
  <div class="note-line" style="top:355px"></div>
  <div class="note-line" style="top:398px"></div>
  <div class="note-line" style="top:437px"></div>
  <div class="footer-rule"></div>
  <div class="web-tab">www.rudyfenwick.example</div>
</section>

<section class="flyer flyer--back" aria-label="Flyer back">
  <div class="back-scene" role="img" aria-label="Faint washed-out photo of Rudy Fenwick standing in a bright hallway"></div>
  <div class="back-header">
    <div class="brand-name">Rudy <span class="underlined">Fenwick</span></div>
  </div>
  <div class="contact-bar">
    <span>Australia +61 400 000 000 <span class="sep"></span>Singapore: +65 9000 0000</span>
    <span class="contact-bar__email">
      <svg width="10" height="10" viewBox="0 0 10 10" aria-hidden="true"><circle cx="5" cy="5" r="4.4" fill="none" stroke="#d6d6d6" stroke-width="0.7"/><rect x="2.6" y="3.4" width="4.8" height="3.3" fill="none" stroke="#d6d6d6" stroke-width="0.6"/><path d="M2.6 3.4 L5 5.3 L7.4 3.4" fill="none" stroke="#d6d6d6" stroke-width="0.6"/></svg>
      rudy@rudyfenwick.example
    </span>
  </div>
  <div class="note-line" style="top:117px"></div>
  <div class="note-line" style="top:154px"></div>
  <div class="note-line" style="top:197px"></div>
  <div class="note-line" style="top:240px"></div>
  <div class="note-line" style="top:277px"></div>
  <div class="note-line" style="top:318px"></div>
  <div class="note-line" style="top:353px"></div>
  <div class="note-line" style="top:391px"></div>
  <div class="note-line" style="top:436px"></div>
  <div class="web-tab">www.rudyfenwick.example</div>
</section>

</body>
</html>
```